Email Banner for Technology Company

We need a new email banner. The purpose of the email banner is to make us look more professional as a business and keep all communications with clients uniform. The previous designs which we have included below have now become outdated as our brand has developed and we need the new banner to become more aligned and modern.

We are a marketing organization that specialises in lead generation, email newsletters are sent to prospects on a regular basis. Therefore, it is important that we have an aesthetically pleasing banner as this is the first real impression prospects have our business. First impressions matter.

We are looking for a new email banner design as the current design is now outdated and does not reflect who we are as a business.

The new banners are required for launch at the start of Q2.

There is future work in the pipeline for the winning design. We have multiple industry sites that will require the new design as well as creating each of these in multiple languages.

The design must include the Zentroval wording the tagline 'The Ultimate Research Library for Technology Pro's.
It needs to be creative and fun but still remain professional, sticking with the colour theme that already exists.

Requirements
Must have
• The design must include the Zentroval wording the tagline 'The Ultimate Research Library for Technology Pro's.

```html
<!DOCTYPE html>
<html lang="en">
<head>
<meta charset="utf-8">
<title>Zentroval – Email Banner Concepts</title>
<link rel="stylesheet" href="https://fonts.googleapis.com/css2?family=Roboto+Slab:wght@300;400;700&display=swap">
<style>
  :root {
    --page: #ffffff;
    --frame: #111111;
    --royal: #2446a8;
    --royal-deep: #1c3490;
    --royal-light: #3062c0;
    --cyan: #00b0ee;
    --teal: #1db5a6;
    --mist: #ececec;
    --mist-edge: #fafafa;
    --slate: #555555;
    --navy: #0f1230;
    --electric: #1e8fd8;
    --white: #ffffff;
  }
  * { margin: 0; padding: 0; box-sizing: border-box; }
  html, body { width: 1200px; height: 689px; overflow: hidden; background: var(--page); }
  .canvas {
    position: relative; width: 1200px; height: 689px;
    border: 1px solid var(--frame); background: var(--page);
    font-family: "Roboto Slab", Georgia, serif;
  }
  .banner { position: absolute; left: 71px; width: 1058px; height: 173px; overflow: hidden; }

  /* Concept 1: royal blue diagonal */
  .banner--diagonal { top: 59px; background: var(--royal); }
  .banner--diagonal svg { position: absolute; inset: 0; }
  .banner--diagonal .brand-name {
    position: absolute; left: 28px; top: 82px;
    font-weight: 700; font-size: 52px; line-height: 1; letter-spacing: 10px;
    color: var(--cyan); text-transform: uppercase;
  }
  .banner--diagonal .tagline {
    position: absolute; right: 24px; top: 79px; text-align: right;
    font-weight: 300; font-size: 19px; line-height: 23px; color: var(--teal);
  }

  /* Concept 2: light circuit */
  .banner--light { top: 258px; border: 1px solid var(--frame); }
  .banner--light .backdrop {
    position: absolute; inset: 0;
    background: radial-gradient(ellipse 45% 110% at 50% 100%, var(--mist) 0%, #e4e4e4 60%, var(--mist-edge) 100%);
  }
  .banner--light .brand-name {
    position: absolute; left: 0; right: 0; top: 50px; text-align: center;
    font-weight: 400; font-size: 56px; line-height: 1; color: var(--cyan);
  }
  .banner--light .tagline {
    position: absolute; left: 0; right: 0; top: 116px; text-align: center;
    font-weight: 300; font-size: 17px; color: var(--slate);
  }

  /* Concept 3: dark tech portal */
  .banner--dark { top: 456px; left: 72px; width: 1057px; height: 171px; }
  .banner--dark .backdrop {
    position: absolute; inset: 0;
    background: radial-gradient(ellipse 28% 95% at 51% 60%, #0c1440 0%, #145aa8 45%, var(--electric) 58%, #16307a 72%, var(--navy) 88%);
  }
  .banner--dark .brand-name {
    position: absolute; left: 392px; top: 80px;
    font-weight: 700; font-size: 44px; line-height: 1; letter-spacing: 8px;
    color: var(--white); text-transform: uppercase;
  }
  .banner--dark .tagline {
    position: absolute; left: 30px; top: 72px;
    font-weight: 300; font-size: 20px; line-height: 26.5px; color: var(--white);
  }
</style>
</head>
<body>
<div class="canvas">

  <section class="banner banner--diagonal">
    <svg width="1058" height="173" viewBox="0 0 1058 173" aria-hidden="true">
      <defs>
        <linearGradient id="band-sheen" x1="0" y1="0" x2="1" y2="0">
          <stop offset="0" stop-color="#1f3c9c"/>
          <stop offset="1" stop-color="#2b58b8"/>
        </linearGradient>
      </defs>
      <rect width="1058" height="173" fill="var(--royal)"/>
      <polygon points="420,0 640,0 814,173 594,173" fill="url(#band-sheen)"/>
      <polygon points="640,0 1058,0 1058,173 814,173" fill="var(--royal-light)"/>
      <polygon points="700,0 1058,0 1058,60 760,60" fill="#2c5cbc" opacity="0.7"/>
      <polygon points="560,0 640,0 814,173 734,173" fill="var(--royal-deep)" opacity="0.8"/>
      <rect x="0" y="18" width="190" height="12" fill="var(--royal-deep)" opacity="0.7"/>
      <rect x="0" y="52" width="600" height="2" fill="#4aa6f0" opacity="0.6"/>
      <rect x="0" y="4" width="250" height="2" fill="#4aa6f0" opacity="0.5"/>
      <rect x="740" y="23" width="318" height="2" fill="#4aa6f0" opacity="0.6"/>
      <rect x="800" y="8" width="258" height="2" fill="#6ec0f5" opacity="0.6"/>
    </svg>
    <div class="brand-name">Zentroval</div>
    <p class="tagline">The Ultimate Research Library<br>for Technology Pro’s</p>
  </section>

  <section class="banner banner--light">
    <div class="backdrop" role="img" aria-label="Light grey circuit-board arcs and trace lines background"></div>
    <div class="brand-name">Zentroval</div>
    <p class="tagline">The Ultimate Research Library for Technology Pro’s</p>
  </section>

  <section class="banner banner--dark">
    <div class="backdrop" role="img" aria-label="Dark navy futuristic portal with glowing blue rings background"></div>
    <p class="tagline">The Ultimate<br>Research Library for<br>Technology Pro’s</p>
    <div class="brand-name">Zentroval</div>
  </section>

</div>
</body>
</html>
```